Amber Ladle Whimsy Website Design; Cupcake Business with a unique and bespoke design element

We need a website design for a new bespoke and unique business making gourmet cupcakes - but MOST IMPORTANTLY we design and handmake cupcake wrappers and toppers specifically for each client's event. We are based in Sydney, Australia. The final resulting website should be elegant yet whimsical reflecting the notion of dreams and very elegant events eg weddings and very special parties.

We want to eventually have about 5 pages, HOWEVER, this project is specifically for the first page (ie Home page) and one other only. The final required pages are: a HOME page; ABOUT US page; PHOTO GALLERY page; FLAVOUR MENU & OTHER PRODUCTS page; CONTACT & INTERNET ENQUIRY page.

We expect the HOME page to be quite elaborate, perhaps including some animation. We will be providing the text content for all the other pages, and basically they will have the same background as the home page. We are looking for a clean design that runs across each page thus giving the website a continuity that pulls it all together. We would like our logo to be included on each page.

PLEASE NOTE: We will want multiple pages worked on in the handover phase but initially we want a very concise, consistent template to limit the amount of work to prospective designers.

While we are primarily looking for the design phase to be covered by this project, we would certainly appreciate coding to be included and will take that into consideration when choosing a winner.

Hi Designers

We have added some more information to our brief - please review it.

Thanks and happy designing

Hi Designers

Please note that we have increased our Prize money to $750.00.  We hope this encourages you to participate.

Thanks and regards
Amber Ladle Whimsy

Hi Designers

We've just posted some photos to help give you an idea of what we do.  Please note our attention to detail and precision in our work.

Thanks
Amber Ladle Whimsy

Hi Designers

Please Note:  What makes us different  to any other cupcake business is that we design cupcake wrappers and toppers, unique to our client's event whether it be a wedding, a birthday party or product launch.  We consult with our client to understand themes, colours, styles etc.  We then have our designs printed, next they are cut by a specialised computerised cutting machine,  We assemble everything by hand, and usually embellish the wrapper and topper with pearls, crystals, feathers, lace, ribbons or whatever else is appropriate for the event.  All work is totally bespoke, unique and individual.  No other cupcake supplier that we know of goes to these lengths to satisfy their client's dreams.

THE WRAPPER AND TOPPER IS OUR PRIMARY SELLING POINT. 

PLEASE NOTE:- We have uploaded a new photograph which we want to be used as the main photograph on the landing page.

We have removed all previous photographs of cupcakes (except for one that we can't get rid of).

We don't want a picture of a cupcake on the landing page we want the image _D7C3239.jpg to be used for that purpose.

We have also uploaded our logo in a number of file formats as we have had requests from you for these.

Hi designers

we have a crazy busy weekend on and won't be able to make any decisions re our competition until Monday  -  sorry to keep you in suspense, just a couple more days please!

regards
Meg

Target Market(s)

Primarily women - brides, new mothers (Christenings), Event Planners, who place an emphasis on the beauty of a product rather than the cost

Industry/Entity Type

Events

Requirements
Must have
• It must have our Logo (see attached upload) on each page (our logo is a butterfly atop a cupcake resting on a spoon and our motto is "Baking Charming Pieces of Craft". The colours used are pale pink, blue and chocolate brown and we'd expect these colours to be repeated in the final website.
The website must have a photo gallery which we can access and add to/change as our business grows.
We need a contact page which has an "internet enquiry form".
There should be a "Menu" page describing our cupcake flavours.
The Home page must have a party/event feel to it - definitely making an enquirer want to enter further into the site.
Nice to have
• Our logo is attached below in the "uploads". One idea that we have had is to use the butterfly in the logo but start it as a caterpillar crawling on the screen; as it spins it's cocoon the words "Gentle Slumber Tiny Grub" would appear on screen; this would incorporate the "Dreams" in our Business Name; then our logo butterfly would hatch. This encapsulates the idea of taking something plain (caterpillar/cupcake) and creating something beautiful (butterfly/OUR cupcake).
However, we are open to other design ideas.
The colours we would like to have are pale pink, blue and chocolate brown in the design.

Some websites we really admire are: www.dorawhitley.example www.glueribbontart.example.au and www.greetingsvera.example.au
These websites have a lightness and sense of fantasy to them. They do not convey a corporate image at all, rather they make you want to be at the party.
Should not have
• No "Corporate" style.

Most Important: We already have a website which we are not happy with - that is why we are going through this exercise to replace it. That means we DO NOT want anything along the lines of our current website. We are expecting some fresh ideas for our prize money.

```html
<!DOCTYPE html>
<html lang="en">
<head>
<meta charset="utf-8">
<title>Amber Ladle Whimsy</title>
<link href="https://fonts.googleapis.com/css2?family=Noto+Sans:wght@400;700&display=swap" rel="stylesheet">
<style>
  :root {
    --page-pink: #fcdce0;
    --panel-white: #fefafb;
    --tab-pink: #fbd3da;
    --tab-text: #3d4a5c;
    --footer-pink: #fbaab6;
    --heading-blue: #1a7fc9;
    --body-ink: #151515;
    --brand-brown: #5a3a2a;
    --photo-pink: #f3a9c0;
    --photo-light: #fbe6ee;
  }
  * { margin: 0; padding: 0; box-sizing: border-box; }
  html, body { width: 1200px; height: 973px; overflow: hidden; }
  body {
    position: relative;
    background: var(--page-pink);
    font-family: "Noto Sans", sans-serif;
    color: var(--body-ink);
  }
  .brand {
    position: absolute;
    left: 0; width: 1200px; top: 178px; height: 56px;
    display: flex; justify-content: center; align-items: center; gap: 16px;
  }
  .brand-dot {
    width: 18px; height: 18px; border-radius: 50%;
    background: var(--heading-blue);
  }
  .brand-name {
    font-family: "Noto Sans", sans-serif;
    font-size: 42px;
    font-weight: 400;
    line-height: 1;
    color: var(--brand-brown);
  }
  .content-panel {
    position: absolute;
    left: 107px; top: 284px; width: 977px; height: 619px;
    background: var(--panel-white);
    border-radius: 10px;
  }
  .hero-photo {
    position: absolute;
    left: 14px; top: 21px; width: 391px; height: 572px;
    background: linear-gradient(180deg, var(--photo-light) 0%, #f6c7d6 45%, var(--photo-pink) 100%);
  }
  .main-nav {
    position: absolute; top: 18px; left: 0; width: 100%; height: 33px;
  }
  .main-nav a {
    position: absolute; top: 0; height: 33px;
    background: var(--tab-pink);
    border-radius: 8px 8px 0 0;
    color: var(--tab-text);
    font-size: 14.5px; font-weight: 700; letter-spacing: 0.8px;
    text-decoration: none;
    display: flex; align-items: center; justify-content: center;
  }
  .tab-menu { left: 434px; width: 152px; }
  .tab-gallery { left: 595px; width: 158px; }
  .tab-enquiry { left: 761px; width: 191px; }
  .intro {
    position: absolute; left: 443px; top: 96px; width: 500px;
  }
  .intro h1 {
    font-size: 29px; font-weight: 700; letter-spacing: 1.6px;
    color: var(--heading-blue); line-height: 1;
  }
  .intro .tagline {
    margin: 7px 0 0 2px;
    font-size: 13px; font-weight: 700; letter-spacing: 0.8px;
  }
  .intro p.copy {
    margin-top: 34px;
    font-size: 14px; line-height: 16.4px; letter-spacing: 0.35px;
    width: 492px;
  }
  .intro p.copy + p.copy { margin-top: 16px; }
  .site-footer {
    position: absolute; left: 0; top: 912px; width: 1200px; height: 61px;
    background: var(--footer-pink);
    font-size: 14.5px;
  }
  .footer-links { position: absolute; left: 105px; top: 27px; }
  .footer-links a { color: var(--body-ink); text-decoration: none; }
  .copyright { position: absolute; left: 817px; top: 19px; }
</style>
</head>
<body>
  <header class="brand">
    <span class="brand-dot"></span>
    <span class="brand-name">Amber Ladle Whimsy</span>
  </header>

  <main class="content-panel">
    <div class="hero-photo" role="img" aria-label="Tiered stand of pink cupcakes with ballerina dress toppers and tulle skirts for a fifth birthday"></div>

    <nav class="main-nav">
      <a class="tab-menu" href="#">FLAVOUR MENU</a>
      <a class="tab-gallery" href="#">PHOTO GALLERY</a>
      <a class="tab-enquiry" href="#">INTERNET ENQUIRY</a>
    </nav>

    <section class="intro">
      <h1>AMBER LADLE WHIMSY</h1>
      <p class="tagline">BAKING CHARMING PIECES OF CRAFT</p>
      <p class="copy">Amber Ladle Whimsy is a gourmet cupcake service based in Fernvale, Sydney, specialising in artistic creations focusing heavily on design, colour, theme and most importantly taste!</p>
      <p class="copy">We handcraft the best cupcakes that you have ever tasted and they're beautiful too.&nbsp; Our cupcake toppers and wrappers are designed personally for your event making them a unique work of art that have the WOW factor.&nbsp; It's not just a cupcake &nbsp;- &nbsp;Amber Ladle Whimsy are indulgent, luxurious, chic and delicious.</p>
      <p class="copy">We are experts in selecting just the right colours and accents to match your colour palette, theme, or company logo.&nbsp; Everything we do is completely bespoke and we use colour/fabric swatches, floral arrangements, invitations or even just an idea to create a display at your event which will have your guests talking for weeks!&nbsp; We work with you every step of the way to make sure that your cupcakes will not only meet your requirements but exceed your expectations too.</p>
    </section>
  </main>

  <footer class="site-footer">
    <div class="footer-links"><a href="#">Products</a> &nbsp;/ <a href="#">Menu Gallery</a> &nbsp;/ &nbsp;<a href="#">FAQ &amp; Testimonails</a> <a href="#">Contact</a></div>
    <div class="copyright">© Copyright Amber Ladle Whimsy 2011</div>
  </footer>
</body>
</html>
```